Velmora Steam Cleaning website for demos

Velmora Steam Cleaning is a business that provides commercial cleaning services utilizing steam vapor, which offers the most effective and ecologically friendly method of cleaning today. We need a website to advertise our services, and needs to incorporate spaces to show video demonstrations on how the cleaning machine works.

Target Market(s)

The potential market for this business are hotels, motels, restaurants, hospitals, fast food facilities, nursing homes, day care centers, schools, country clubs, churches, office and apartment buildings, malls, movie theaters, super markets, airports, parks, and any other facility.

Industry/Entity Type

Business

Coding

Coded - Design and coding required

Number of Pages Required

3 page

Colors
add136
9bcb3c
34a6d7
3176b5
edf8f6

Requirements
Must have
• Areas for videos that serve as demonstrations of our services

```html
<!DOCTYPE html>
<html lang="en">
<head>
<meta charset="utf-8">
<title>Velmora Steam Cleaning</title>
<link href="https://fonts.googleapis.com/css2?family=Exo+2:wght@400;500;600&family=Roboto:wght@400;500&display=swap" rel="stylesheet">
<style>
:root{
  --green:#9bcb3c;
  --green-dark:#add136;
  --sky:#34a6d7;
  --navy:#3176b5;
  --mint:#edf8f6;
  --ink:#1c1c1c;
  --text:#555;
  --band:#3d9ad0;
  --foot:#111;
  --foot-deep:#080808;
  --muted:#8a8a8a;
}
*{box-sizing:border-box;margin:0;padding:0}
html,body{width:1200px;height:2372px;overflow:hidden}
body{position:relative;background:#fff;font-family:"Roboto",Arial,sans-serif;color:var(--text)}
.abs{position:absolute}
h1,h2,h3,h4{font-family:"Exo 2",Arial,sans-serif;font-weight:500}

/* top bar */
.topbar{left:0;top:0;width:1200px;height:42px;background:var(--foot);color:#ddd;font-size:12px;display:flex;justify-content:flex-end;align-items:center;gap:22px;padding-right:112px}
.topbar span{display:flex;align-items:center;gap:6px}

/* header */
.header{left:0;top:42px;width:1200px;height:106px;background:#fff}
.brand{left:111px;top:36px;display:flex;align-items:center;gap:10px}
.brand-dot{width:34px;height:34px;border-radius:50%;background:var(--green)}
.brand-name{font-family:"Exo 2",Arial,sans-serif;font-weight:600;font-size:22px;color:var(--navy)}
.nav{right:111px;top:48px;display:flex;gap:44px;font-size:12.5px;font-weight:500;color:#222}
.nav .active{color:var(--navy)}

/* hero */
.hero{left:0;top:148px;width:1200px;height:600px;background:linear-gradient(100deg,#b9b7b1 0%,#d6d4ce 40%,#cfcac2 65%,#ecefee 100%)}
.hero-caption{left:112px;top:492px;width:655px;height:80px;background:rgba(240,240,240,.88);display:flex;align-items:center;padding-left:24px;font-family:"Exo 2",Arial,sans-serif;font-size:30px;font-weight:500;color:#222}
.hero-arrow{width:22px;height:22px;border-radius:50%;background:#555;top:451px}

/* features */
.features{left:112px;top:660px;width:976px;height:242px;display:flex;box-shadow:0 22px 28px -18px rgba(0,0,0,.45)}
.feature{flex:1;color:#fff;text-align:center;padding:20px 12px 0}
.feature:nth-child(odd){background:var(--sky)}
.feature:nth-child(even){background:var(--navy)}
.feature-icon{width:64px;height:64px;border:2px solid #fff;border-radius:50%;margin:0 auto 16px;display:flex;align-items:center;justify-content:center}
.feature h3{font-family:"Roboto",Arial,sans-serif;font-weight:400;font-size:17px;line-height:21px;margin-bottom:10px}
.feature p{font-size:12px;line-height:21px;color:#e6f2fa}

/* welcome */
.welcome{left:130px;top:950px;width:940px;text-align:center}
.welcome h2{font-size:27px;color:var(--navy);margin-bottom:14px}
.welcome p{font-size:11.5px;line-height:25.5px}

/* how it works */
.how{left:0;top:1115px;width:1200px;height:264px;background:var(--mint)}
.how h2{position:absolute;left:111px;top:28px;font-size:22px;color:var(--navy)}
.how p{position:absolute;left:111px;top:66px;width:645px;font-size:11.5px;line-height:25.5px}
.btn{position:absolute;left:112px;top:197px;width:107px;height:40px;background:var(--sky);color:#fff;font-size:12px;display:flex;align-items:center;justify-content:center}
.video{position:absolute;left:786px;top:25px;width:302px;height:207px;background:#fff;border:1px solid #ddd;padding:5px}
.video-frame{width:100%;height:165px;background:linear-gradient(135deg,#cfd8de,#8b979f 55%,#3a4248)}
.video-bar{height:28px;display:flex;align-items:center;gap:6px;padding:0 4px}
.ctl{height:16px;border:1px solid #ccc;background:#f4f4f4}

/* columns */
.col{width:306px;text-align:center}
.col h3{font-size:20px;color:var(--navy);margin-bottom:13px}
.col-photo{height:169px;border:4px solid #fff;box-shadow:0 0 0 1px #ddd}
.col p{font-size:11.5px;line-height:25.5px;margin-top:20px}

/* services */
.services{left:0;top:1755px;width:1200px;height:340px;background:linear-gradient(120deg,#4aa5d8,#3d9ad0 50%,#3a8fc6)}
.services h2{position:absolute;top:38px;width:100%;text-align:center;font-size:26px;color:#fff}
.services .lead{position:absolute;left:215px;top:80px;width:770px;text-align:center;font-size:11.5px;line-height:23px;color:#fff}
.svc{position:absolute;top:150px;width:223px;height:141px;border:3px solid #cfe7f4}
.svc-overlay{background:#2a2a2a;color:#fff;text-align:center;padding:14px 10px}
.svc-overlay h4{font-family:"Roboto",Arial,sans-serif;font-size:14.5px;font-weight:500;margin-bottom:6px}
.svc-overlay p{font-size:12px;line-height:21px;color:#ddd}
.svc-arrow{position:absolute;top:180px}

/* footer */
.footer{left:0;top:2095px;width:1200px;height:221px;background:var(--foot);color:var(--muted);font-size:11.5px}
.fcol{position:absolute;top:30px}
.fcol h4{font-size:17px;color:#fff;margin-bottom:12px}
.post{display:flex;gap:10px;margin-bottom:14px}
.post-photo{width:73px;height:52px}
.post b{display:block;color:#fff;font-weight:400;font-size:12px;margin-bottom:5px}
.post span{line-height:17px;display:block;width:170px}
.links{display:grid;grid-template-columns:143px 120px;row-gap:10px}
.contact li{list-style:none;display:flex;gap:10px;margin-bottom:10px;line-height:17px}
.social li{list-style:none;display:flex;align-items:center;gap:8px;margin-bottom:10px}
.sq{width:13px;height:13px;display:inline-block}
.bottom{left:0;top:2316px;width:1200px;height:56px;background:var(--foot-deep);color:#666;font-size:11px;display:flex;align-items:center;justify-content:center}
</style>
</head>
<body>

<div class="abs topbar">
  <span><svg width="10" height="13" viewBox="0 0 10 13"><path d="M5 0a5 5 0 0 0-5 5c0 3.5 5 8 5 8s5-4.5 5-8a5 5 0 0 0-5-5z" fill="#9bcb3c"/><circle cx="5" cy="5" r="2" fill="#111"/></svg>48 Harbor Lane Ste. 12-204 Brookfield, NY 10452</span>
  <span><svg width="13" height="13" viewBox="0 0 13 13"><rect width="13" height="13" rx="2" fill="#9bcb3c"/><path d="M4 3l1.5 2-1 1a5 5 0 0 0 2.5 2.5l1-1 2 1.5-1 1.5C6 10 3 7 2.5 4.5z" fill="#111"/></svg>555 010 2040</span>
</div>

<header class="abs header">
  <div class="abs brand"><span class="brand-dot"></span><span class="brand-name">Velmora Steam Cleaning</span></div>
  <nav class="abs nav"><span class="active">HOME</span><span>ABOUT US</span><span>SERVICES</span><span>OPPORTUNITIES</span><span>BENEFITS</span><span>NEWS</span><span>CONTACT US</span></nav>
</header>

<section class="abs hero" role="img" aria-label="Technician in a blue shirt steam-cleaning carpet in a bright empty room"></section>
<div class="abs hero-arrow" style="left:34px"><svg width="22" height="22"><path d="M13 6l-5 5 5 5" stroke="#fff" stroke-width="2" fill="none"/></svg></div>
<div class="abs hero-arrow" style="left:1147px"><svg width="22" height="22"><path d="M9 6l5 5-5 5" stroke="#fff" stroke-width="2" fill="none"/></svg></div>
<div class="abs hero-caption">SAFE AND ECO-FRIENDLY GREEN CLEANING</div>

<section class="abs features">
  <div class="feature">
    <div class="feature-icon"><svg width="30" height="30" viewBox="0 0 30 30" fill="none" stroke="#fff" stroke-width="2"><path d="M15 4c5 7 8 11 8 15a8 8 0 0 1-16 0c0-4 3-8 8-15z"/><path d="M6 6l18 18"/></svg></div>
    <h3>No chemicals or soaps<br>involved</h3>
    <p>Lorem ipsum dolor sit amet, conse ctetuer adipiscing elit, sed diam nonum my nibh euismod.</p>
  </div>
  <div class="feature">
    <div class="feature-icon" style="border:none"><svg width="40" height="40" viewBox="0 0 40 40" fill="none" stroke="#fff" stroke-width="2"><path d="M20 4c-4 5-4 10 0 14 4-4 4-9 0-14z"/><path d="M6 20c6 0 12 4 14 10 2-6 8-10 14-10v10c-6 0-12 3-14 7-2-4-8-7-14-7z"/></svg></div>
    <h3>Safe and eco-friendly Green<br>Cleaning</h3>
    <p>Ut wisi enim ad minim veniam, quis nostrud exerci tation ullamcorper suscipit lobortis.</p>
  </div>
  <div class="feature">
    <div class="feature-icon" style="border:none"><svg width="40" height="40" viewBox="0 0 40 40" fill="none" stroke="#fff" stroke-width="2"><path d="M8 6c0 14 4 20 10 24"/><rect x="18" y="20" width="16" height="14" rx="6"/><circle cx="26" cy="30" r="2"/></svg></div>
    <h3>Cleans, Sanitizes, Deodorizes<br>and Disinfects</h3>
    <p>Duis autem vel eum iriure dolor in hendrerit in vulputate velit esse mo lestie consequat.</p>
  </div>
  <div class="feature">
    <div class="feature-icon"><svg width="34" height="34" viewBox="0 0 34 34" fill="#fff" stroke="#fff" stroke-width="1.6"><circle cx="17" cy="17" r="4"/><path d="M17 17L17 5M17 17L28 11M17 17L27 25M17 17L17 29M17 17L7 24M17 17L6 11"/><circle cx="17" cy="5" r="2"/><circle cx="28" cy="11" r="2"/><circle cx="27" cy="25" r="2"/><circle cx="17" cy="29" r="2"/><circle cx="7" cy="24" r="2"/><circle cx="6" cy="11" r="2"/></svg></div>
    <h3>Causes No Allergies</h3>
    <p>Typi non habent claritatem insitam; est usus legentis in iis qui facit eorum claritatem. Investigationes de mo straverunt lectores.</p>
  </div>
</section>

<section class="abs welcome">
  <h2>WELCOME TO VELMORA STEAM CLEANING</h2>
  <p>Duis autem vel eum iriure dolor in hendrerit in vulputate velit esse molestie consequat, vel illum dolore eu feugiat nulla facilisis at vero eros et accumsan et iusto odio dignissim qui blandit praesent luptatum zzril delenit augue duis dolore te feugait nulla facilisi. Nam liber tempor cum soluta nobis eleifend option congue nihil imperdiet doming id quod mazim placerat facer possim assum. Typi non habent claritatem insitam; est usus legentis in iis qui facit eorum claritatem. placerat facer possim assum. Typi non habent claritatem insitam; est usus legentis in iis qui facit eorum claritatem.</p>
</section>

<section class="abs how">
  <h2>HOW IT WORKS?</h2>
  <p>Ut wisi enim ad minim veniam, quis nostrud exerci tation ullamcorper suscipit lobortis nisl ut aliquip ex ea commodo consequat. Duis autem vel eum iriure dolor in hendrerit in vulputate velit esse molestie consequat, vel illum dolore eu feugiat nulla facilisis at vero eros et accumsan et iusto odio dignissim qui blandit praesent luptatum zzril delenit augue duis dolore te feugait nulla facilisi. Nam liber tempor cum soluta nobis eleifend option congue nihil imperdiet doming id quod mazim placerat facer possim assum. Typi non habent claritatem insitam.</p>
  <span class="btn">READ MORE</span>
  <div class="video">
    <div class="video-frame" role="img" aria-label="Demonstration video: gloved hand steam-cleaning a tiled wall"></div>
    <div class="video-bar">
      <span class="ctl" style="width:16px"></span>
      <span class="ctl" style="width:40px"></span>
      <span class="ctl" style="width:50px;background:linear-gradient(90deg,#f08a1c 60%,#f4f4f4 60%)"></span>
      <span style="flex:1"></span>
      <span class="ctl" style="width:40px"></span>
      <span class="ctl" style="width:16px"></span>
      <span class="ctl" style="width:16px;background:var(--green)"></span>
    </div>
  </div>
</section>

<section class="abs col" style="left:112px;top:1424px">
  <h3>BUSINESS AND SERVICES</h3>
  <div class="col-photo" role="img" aria-label="Steam cleaner wand on a large glass window" style="background:linear-gradient(135deg,#6f7d63,#b9c7a8 50%,#3c4a3a)"></div>
  <p>Lorem ipsum dolor sit amet, consectetuer adipiscing elit, sed diam nonummy nibh euismod tincidunt ut laoreet dolore magna aliquam erat volutpat.</p>
</section>
<section class="abs col" style="left:447px;top:1424px">
  <h3>MARKET</h3>
  <div class="col-photo" role="img" aria-label="Steam head lifting dust from a carpet" style="background:linear-gradient(135deg,#6d6358,#b9aa98 50%,#8a7c6c)"></div>
  <p>Lorem ipsum dolor sit amet, consectetuer adipiscing elit, sed diam nonummy nibh euismod tincidunt ut laoreet dolore magna aliquam erat volutpat.</p>
</section>
<section class="abs col" style="left:780px;top:1424px">
  <h3>BEST SUPPORT</h3>
  <div class="col-photo" role="img" aria-label="Technician with steam equipment on outdoor stairs" style="background:linear-gradient(90deg,#8c7a5c,#a39170 55%,#8b3a2c)"></div>
  <p>Lorem ipsum dolor sit amet, consectetuer adipiscing elit, sed diam nonummy nibh euismod tincidunt ut laoreet dolore magna aliquam erat volutpat.</p>
</section>

<section class="abs services">
  <h2>OUR SERVICES</h2>
  <p class="lead">Duis autem vel eum iriure dolor in hendrerit in vulputate velit esse molestie consequat, vel illum dolore eu feugiat nulla facilisis at vero eros et accumsan et iusto odio dignissim qui blandit praesent luptatum zzril delenit augue duis dolore te feugait nulla facilisi. Nam liber tempor.</p>
  <svg class="svc-arrow" style="left:62px" width="18" height="36"><path d="M16 2L2 18l14 16" stroke="#cfe7f4" stroke-width="2" fill="none"/></svg>
  <div class="svc" style="left:112px" role="img" aria-label="Steam jet cleaning a glass surface" data-fill="1"><div style="width:100%;height:100%;background:linear-gradient(135deg,#c9d6dc,#6f7f86)"></div></div>
  <div class="svc" style="left:362px" role="img" aria-label="Worker steam-cleaning industrial machinery"><div style="width:100%;height:100%;background:linear-gradient(135deg,#8c9398,#3d4448)"></div></div>
  <div class="svc svc-overlay" style="left:613px">
    <h4>AUTO STEAM CLEANING</h4>
    <p>Lorem ipsum dolor sit amet, conse ctetuer adipiscing elit, sed diam nonummy nibh euismod.</p>
    <svg width="18" height="18" style="margin-top:6px"><circle cx="9" cy="9" r="9" fill="#fff"/><path d="M5 9h7M9 5l4 4-4 4" stroke="#2a2a2a" stroke-width="2" fill="none"/></svg>
  </div>
  <div class="svc" style="left:863px" role="img" aria-label="Steam mop on a stone floor"><div style="width:100%;height:100%;background:linear-gradient(135deg,#d9d6d0,#a9a49c)"></div></div>
  <svg class="svc-arrow" style="left:1120px" width="18" height="36"><path d="M2 2l14 16L2 34" stroke="#cfe7f4" stroke-width="2" fill="none"/></svg>
</section>

<footer class="abs footer">
  <div class="fcol" style="left:111px">
    <h4>OUR BLOG</h4>
    <div class="post"><div class="post-photo" role="img" aria-label="Blog post photo of floor cleaning" style="background:linear-gradient(135deg,#ddd,#888)"></div><div><b>Lorem ipsum dolor sit</b><span>Ut wisi enim ad minim veniam, quis nostrud...</span></div></div>
    <div class="post"><div class="post-photo" role="img" aria-label="Blog post photo of steam mop" style="background:linear-gradient(135deg,#e2ddd6,#a39a90)"></div><div><b>Lorem ipsum dolor sit</b><span>Ut wisi enim ad minim veniam, quis nostrud...</span></div></div>
  </div>
  <div class="fcol" style="left:410px">
    <h4>QUICK LINKS</h4>
    <div class="links"><span>Home</span><span>Gallery</span><span>About Us</span><span>Privacy Policy</span><span>Cleaning Services</span><span>Sitemap</span><span>Latest News</span><span>Terms &amp; Conditions</span><span>Contact Us</span></div>
  </div>
  <div class="fcol" style="left:719px">
    <h4>CONTACT US</h4>
    <ul class="contact">
      <li><svg width="10" height="13" viewBox="0 0 10 13"><path d="M5 0a5 5 0 0 0-5 5c0 3.5 5 8 5 8s5-4.5 5-8a5 5 0 0 0-5-5z" fill="#9bcb3c"/></svg><span>VELMORA STEAM CLEANING<br>48 Harbor Lane Ste. 12-204<br>Brookfield, NY 10452</span></li>
      <li><svg width="14" height="10"><rect width="14" height="10" fill="#9bcb3c"/><path d="M0 0l7 5 7-5" stroke="#111" fill="none"/></svg><span>velmorasteam.com</span></li>
      <li style="margin-top:14px"><svg width="13" height="13"><rect width="13" height="13" rx="2" fill="#9bcb3c"/></svg><span>555 010 2040</span></li>
    </ul>
  </div>
  <div class="fcol" style="left:987px">
    <h4>CONNECT US</h4>
    <ul class="social">
      <li><span class="sq" style="background:#3b5998"></span>Facenote</li>
      <li><span class="sq" style="background:#34a6d7"></span>Chirper</li>
      <li><span class="sq" style="background:#3176b5"></span>Linkline</li>
      <li><span class="sq" style="background:#d6492f"></span>Globe+</li>
      <li><span class="sq" style="background:#f08a1c"></span>RSS</li>
    </ul>
  </div>
</footer>
<div class="abs bottom">Copyrights @ 2015 Velmora Steam Cleaning . All Right Reserved.</div>

</body>
</html>
```